Flyer für Tiertherapeutin
Eine sehr motivierte und kreative Designerin. Schon der erste Vorschlag war ganz nach meinen Vorstellungen.
Zielgruppe
Ich bin Tiertherapeutin für TCVM und Ernährungsberaterin für Hunde und Katzen. Mittels Akupunktur, Lasertherapie, Mykotherapie und Ernährungsberatung kommt es zu einer Linderung vorhandener Schmerzen, eine verbesserte Regulation der Organe und einer Steigerung das Wohlbefindens sowie Lebensqualität.
Zielgruppe sind überwiegend weibliche Hunde- und Katzenbesitzer mit erkrankten Tieren.
Aufgabenstellung
Flyer sollte klappbar sein. Logo und mein Name und Kontaktdaten sollten enthalten sein.

```html
<!DOCTYPE html>
<html lang="de">
<head>
<meta charset="utf-8">
<title>Pfotenzeit – Flyer</title>
<link href="https://fonts.googleapis.com/css2?family=Open+Sans:wght@400;600;700&family=Yesteryear&display=swap" rel="stylesheet">
<style>
  :root {
    --tan: #cf9a68;
    --tan-text: #c98f5c;
    --dark: #4b4233;
    --ink: #1e1e1e;
    --box: #eceff3;
    --white: #ffffff;
  }
  * { margin: 0; padding: 0; box-sizing: border-box; }
  html, body { width: 1200px; height: 635px; overflow: hidden; background: var(--white); }
  body { font-family: "Open Sans", Arial, sans-serif; color: var(--ink); }
  .flyer { position: relative; width: 1200px; height: 635px; overflow: hidden; background: var(--white); }
  .flyer > * { position: absolute; }

  .cover-photo {
    left: 895px; top: 0; width: 305px; height: 520px;
    background:
      linear-gradient(180deg, rgba(255,255,255,0.95) 0%, rgba(255,255,255,0.75) 30%, rgba(255,255,255,0) 48%),
      linear-gradient(160deg, #e9e4d6 0%, #b9b48c 38%, #c58a4f 62%, #a4703f 78%, #b9a58b 100%);
  }
  .bands { left: 0; top: 0; width: 1200px; height: 635px; }

  .script-title { font-family: "Yesteryear", cursive; color: var(--tan-text); font-weight: 400; font-size: 25px; line-height: 30px; top: 39px; }
  .body-text { font-size: 8.2px; line-height: 14.9px; text-align: justify; width: 247px; }
  .list-title { font-size: 8.4px; line-height: 12px; font-weight: 700; }
  .topic-box { background: var(--box); border-radius: 10px; width: 250px; }
  .topic-box ul { list-style: none; }
  .topic-box li { position: relative; font-size: 8.4px; line-height: 11.7px; padding-left: 30px; padding-right: 2px; margin-bottom: 4.3px; white-space: nowrap; }
  .topic-box li::before { content: ""; position: absolute; left: 12px; top: 4px; width: 3.5px; height: 3.5px; border-radius: 50%; background: var(--ink); }

  .laser-title { left: 28px; }
  .laser-intro { left: 28px; top: 81px; }
  .laser-more { left: 28px; top: 185px; }
  .laser-list-title { left: 28px; top: 261px; }
  .laser-box { left: 25px; top: 281px; height: 147px; padding-top: 7px; }

  .food-title { left: 318px; }
  .food-intro { left: 318px; top: 81px; }
  .food-list-title { left: 318px; top: 217px; }
  .food-box { left: 316px; top: 236px; height: 173px; padding-top: 7px; }
  .food-box li { margin-bottom: 4px; }

  .heart-icon { left: 728px; top: 65px; }
  .contact-intro { left: 626px; width: 250px; top: 97px; text-align: center; }
  .invite { font-size: 8.4px; line-height: 12px; }
  .invite-script { font-family: "Yesteryear", cursive; color: var(--tan-text); font-size: 24px; line-height: 28px; margin-top: 1px; }
  .invite-end { font-size: 8.4px; line-height: 12px; margin-top: -2px; }
  .mode { left: 626px; width: 234px; text-align: center; font-size: 8.4px; line-height: 15px; }
  .mode strong { font-weight: 700; }
  .mode-online { top: 176px; }
  .mode-visit { top: 230px; }

  .photo-circle { width: 186px; height: 186px; border-radius: 50%; border: 5px solid var(--white); }
  .photo-cells { left: 52px; top: 432px; background: radial-gradient(circle at 40% 35%, #fbe8d6 0%, #f0c9a0 45%, #d99a5f 100%); }
  .photo-food { left: 342px; top: 432px; background: radial-gradient(circle at 50% 55%, #b45a3c 0%, #7c3a2b 35%, #3a2a22 70%, #1d1b1a 100%); }

  .contact-block { left: 657px; top: 511px; color: var(--white); font-size: 8.4px; line-height: 15px; font-style: normal; }
  .contact-block .name { font-weight: 700; }
  .contact-block .gap { height: 15px; }

  .brand { left: 915px; width: 270px; top: 148px; text-align: center; }
  .brand-mark { display: inline-block; width: 14px; height: 14px; border-radius: 50%; background: var(--tan); vertical-align: middle; margin-right: 8px; }
  .brand-name { font-weight: 700; font-size: 30px; color: var(--ink); vertical-align: middle; }
  .brand-person { font-weight: 700; font-size: 12px; letter-spacing: 3.5px; margin-top: 10px; color: var(--ink); }

  .offer { left: 900px; width: 300px; top: 529px; text-align: center; color: var(--white); }
  .offer-line { font-size: 18.5px; line-height: 22px; }
  .offer-area { font-size: 12px; margin-top: 7px; }
</style>
</head>
<body>
<main class="flyer">

  <div class="cover-photo" role="img" aria-label="Foto: Katze und Hund liegen nebeneinander im Sonnenlicht"></div>

  <svg class="bands" viewBox="0 0 1200 635" aria-hidden="true">
    <path d="M0,522 C380,482 760,470 1200,476 L1200,635 L0,635 Z" fill="var(--dark)"/>
    <path d="M0,540 C380,494 780,482 1200,486 L1200,635 L0,635 Z" fill="var(--white)"/>
    <path d="M0,553 C360,515 760,492 1200,512 L1200,635 L0,635 Z" fill="var(--tan)"/>
  </svg>

  <h2 class="script-title laser-title">Lasertherapie</h2>
  <p class="body-text laser-intro">Die Lasertherapie beruht auf physikalische Ereignisse. Die La&shy;ser&shy;therapie wirkt von der atomaren Ebene bis zur mikro&shy;sko&shy;pischen Ebene der Gewebe. Durch das gebündelte Laserlicht wird Energie in die Zellen unseres Körpers transportiert. Die Kraftantreiber (Mitochondrien) unserer Zellen nehmen diese Energie auf und bauen sie direkt in Zellenergie um (ATP).</p>
  <p class="body-text laser-more">Die Beeinflussung der Zellenergie fördert alle Lebensvorgänge. Durch die hinzugefügte Energie des Lasers in den Zellen, ist es dem Körper erst möglich wichtige Stoffwechselprozesse voran&shy;zutreiben.</p>
  <h3 class="list-title laser-list-title">Welche Wirkung hat die Lasertherapie?</h3>
  <div class="topic-box laser-box">
    <ul>
      <li>Förderung der Wundheilung, entzündungshemmend<br>durch Anregung des zellulären Stoffwechsels</li>
      <li>Durchblutungsfördernd, antibakteriell</li>
      <li>Anzahl spezifischer Enzyme steigen</li>
      <li>Förderung der Kapillarisation</li>
      <li>Narbenentstörung</li>
      <li>Vermehrung von Kollagenfasern</li>
      <li>Erhöhung der Antikörperbildung</li>
      <li>Verstärkung der Gefäßneubildung</li>
    </ul>
  </div>

  <h2 class="script-title food-title">Ernährungsberatung</h2>
  <p class="body-text food-intro">Ich als Tierernährungsberaterin habe mich auf die Ernährung von Hunden und Katzen spezialisiert und biete dir eine um&shy;fassende Beratung und Unterstützung in Bezug auf die Ernäh&shy;rungs&shy;bedürfnisse deines Tieres. Der Markt an Futtermitteln ist im Laufe der Zeit riesig geworden. Es ist für den Laien teilweise schwierig geworden, zu überprüfen, ob mein Tier wirklich die&shy;ses Futtermittel benötigt oder ob es sich nur um ein Werbever&shy;sprechen handelt.</p>
  <h3 class="list-title food-list-title">Ich berate dich gern zu folgenden Themen:</h3>
  <div class="topic-box food-box">
    <ul>
      <li>Welches Futtermittel ist für mein Tier und den<br>damit verbundenen Bedürfnissen das richtige?</li>
      <li>Entwicklung von Ernährungsplänen: Basierend auf den<br>spezifischen Bedürfnissen deines Tieres</li>
      <li>Gesundheitsmanagement: Adipositas (Fettleibigkeit)<br>oder Kachexie (pathologischer Gewichtsverlust)</li>
      <li>Beratung bei Erkrankungen: Durch gezielte Futter-<br>umstellung die Symptomatik deines Tieres verbessern</li>
      <li>Darmfloraaufbau: Gezielter Darmfloraaufbau lindert<br>Durchfall, hilft deinem Tier ein gesundes Gewicht<br>erreichen, verbessert die Fellqualität und senkt die<br>Infektanfälligkeit</li>
    </ul>
  </div>

  <svg class="heart-icon" width="31" height="31" viewBox="0 0 31 31" aria-hidden="true">
    <circle cx="15.5" cy="15.5" r="15.5" fill="var(--tan)"/>
    <path d="M15.5,23 C8,17.5 7.5,14 8.5,11.5 C10,8.5 14,8.8 15.5,11.5 C17,8.8 21,8.5 22.5,11.5 C23.5,14 23,17.5 15.5,23 Z" fill="var(--white)"/>
  </svg>
  <div class="contact-intro">
    <p class="invite">Neugierig? Jetzt Termin für die</p>
    <p class="invite-script">kostenlose Erstberatung</p>
    <p class="invite-end">vereinbaren.</p>
  </div>
  <p class="mode mode-online"><strong>Online</strong><br>entspannt von zuhause<br>per Videokonferenz</p>
  <p class="mode mode-visit"><strong>Hausbesuche</strong><br>im Raum Karlsruhe auch vor<br>Ort für dich im Einsatz</p>

  <div class="photo-circle photo-cells" role="img" aria-label="Foto: Nahaufnahme leuchtender Zellstrukturen"></div>
  <div class="photo-circle photo-food" role="img" aria-label="Foto: Rohes Fleisch, Gemüse und Karotten in Schalen"></div>

  <address class="contact-block">
    <div class="name">Marlene Vogt</div>
    <div>Birkenallee 12</div>
    <div>76131 Karlsruhe</div>
    <div class="gap"></div>
    <div>0151 - 2384 9067</div>
    <div>info@pfotenzeit-beratung.de</div>
    <div>www.pfotenzeit-beratung.de</div>
  </address>

  <div class="brand">
    <div><span class="brand-mark"></span><span class="brand-name">Pfotenzeit</span></div>
    <div class="brand-person">MARLENE VOGT</div>
  </div>

  <div class="offer">
    <p class="offer-line">Tierernährungsberatung</p>
    <p class="offer-line">TCVM • Akupunktur</p>
    <p class="offer-area">in Karlsruhe und Umgebung</p>
  </div>

</main>
</body>
</html>
```